Criação de Papelaria Profissional para Construção & Engenharia
" Empresa do ramo da engenharia civil com foco projeto, construção, planejamento, gestão e consultoria de obras de construção civil e todo tipo de atividade correlacionada. "

```html
<!DOCTYPE html>
<html lang="pt-BR">
<head>
<meta charset="UTF-8">
<title>Almeida Consultancy — Cartão de visita</title>
<link rel="stylesheet" href="https://fonts.googleapis.com/css2?family=Cormorant+Garamond:wght@600&family=Montserrat:wght@400;500&display=swap">
<style>
  :root {
    --backdrop: #4f6128;
    --card-dark: #232a1f;
    --card-mid: #2c3527;
    --card-back: #2e3a29;
    --gold: #b99262;
    --text-light: #d9dccf;
    --decor: #36432f;
  }
  * { margin: 0; padding: 0; box-sizing: border-box; }
  html, body {
    width: 1200px; height: 1200px; overflow: hidden;
    background: var(--backdrop);
  }
  .canvas {
    position: relative; width: 1200px; height: 1200px;
    display: flex; flex-direction: column; align-items: center; justify-content: center; gap: 60px;
  }
  .card {
    position: relative; width: 760px; height: 400px; overflow: hidden;
    box-shadow: 0 18px 40px rgba(0,0,0,0.35);
  }
  .card-front {
    background: linear-gradient(100deg, var(--card-dark) 0%, var(--card-mid) 55%, var(--card-dark) 100%);
    display: flex; flex-direction: column; align-items: center; justify-content: center;
  }
  .brand-mark {
    width: 52px; height: 52px; border-radius: 50%;
    border: 3px solid var(--gold); margin-bottom: 22px;
  }
  .brand-name {
    font-family: "Cormorant Garamond", serif; font-weight: 600;
    color: var(--gold); font-size: 44px; line-height: 1;
  }
  .brand-tagline {
    font-family: "Montserrat", sans-serif; font-weight: 400;
    color: var(--gold); font-size: 15px; letter-spacing: 0.42em; margin-top: 6px;
  }
  .card-back { background: var(--card-back); }
  .back-decor {
    position: absolute; width: 440px; height: 440px; border-radius: 50%;
    background: var(--decor); right: -40px; top: -40px;
  }
  .back-brand {
    position: absolute; left: 50px; top: 150px;
    display: flex; flex-direction: column; align-items: center;
  }
  .back-brand .brand-mark { width: 32px; height: 32px; border-width: 2px; margin-bottom: 10px; }
  .back-brand .brand-name { font-size: 24px; }
  .back-brand .brand-tagline { font-size: 8px; margin-top: 3px; }
  .contact-list {
    position: absolute; left: 310px; top: 150px; list-style: none;
    font-family: "Montserrat", sans-serif; font-size: 14px; color: var(--text-light);
  }
  .contact-list li { display: flex; align-items: center; gap: 10px; height: 24px; }
  .contact-dot {
    width: 12px; height: 12px; border-radius: 50%; background: var(--gold); flex: none;
  }
</style>
</head>
<body>
<main class="canvas">
  <section class="card card-front" aria-label="Frente do cartão">
    <div class="brand-mark" aria-hidden="true"></div>
    <h1 class="brand-name">Almeida Consultancy</h1>
    <p class="brand-tagline">ENGENHARIA</p>
  </section>

  <section class="card card-back" aria-label="Verso do cartão">
    <div class="back-decor" aria-hidden="true"></div>
    <div class="back-brand">
      <div class="brand-mark" aria-hidden="true"></div>
      <p class="brand-name">Almeida Consultancy</p>
      <p class="brand-tagline">ENGENHARIA</p>
    </div>
    <ul class="contact-list">
      <li>11 90000 4417 <span class="contact-dot" aria-hidden="true"></span></li>
      <li>contato@almeidaconsultancy.eng.br</li>
      <li>almeidaconsultancy.eng.br</li>
      <li><span class="contact-dot" aria-hidden="true"></span>@almeidaconsultancy.eng.br</li>
    </ul>
  </section>
</main>
</body>
</html>
```